Website for Cannabis Investment Fund *

We need to create a website for our fund which invests in cannabis projects

Industry/Entity Type

Cannabis

Coding

Coded - Design and coding required

Number of Pages Required

1 page

Colors

Designer to choose only greyscale colors for use in the design.

Requirements
Must have
• Please see the attached file

```html
<!DOCTYPE html>
<html lang="en">
<head>
<meta charset="utf-8">
<title>Verdant Ridge Capital</title>
<link rel="stylesheet" href="https://fonts.googleapis.com/css2?family=Questrial&family=Raleway:wght@300;400&family=Lato:wght@400;700&family=Tinos&display=swap">
<style>
:root{
  --accent:#2b2b2b;
  --accent-mid:#4a4a4a;
  --ink:#1c1c1c;
  --text:#3a3a3a;
  --muted:#6b6b6b;
  --white:#ffffff;
  --line:#2b2b2b;
}
*{margin:0;padding:0;box-sizing:border-box}
html,body{width:1200px;height:3255px;overflow:hidden}
body{position:relative;background:var(--white);font-family:'Lato',sans-serif;color:var(--text)}
.abs{position:absolute}
.center{left:0;width:1200px;text-align:center}

/* hero */
.hero{top:0;left:0;width:1200px;height:748px;background:radial-gradient(ellipse at 40% 40%,#2e2e2e 0%,#1a1a1a 45%,#0e0e0e 100%)}
.brand{top:6px;left:66px;width:260px;text-align:center;color:var(--white);font-family:'Questrial',sans-serif;font-size:17px;letter-spacing:1px;white-space:nowrap}
.brand-dot{display:block;width:26px;height:26px;border:2px solid var(--white);border-radius:50%;margin:6px auto 10px}
.nav{top:58px;font-size:14px;letter-spacing:1px;color:var(--white)}
.lang{top:20px;left:1039px;width:28px;height:16px;background:#d8d8d8}
.lang-caret{top:26px;left:1079px;border:5px solid transparent;border-top-color:var(--white)}
.video{top:124px;left:265px;width:670px;height:389px;border:3px solid #5a5a5a;background:radial-gradient(ellipse at 50% 45%,#a8a8a8 0%,#6e6e6e 35%,#3a3a3a 70%,#1c1c1c 100%)}
.play{top:278px;left:560px;width:80px;height:80px;border-radius:50%;background:#1e1e1e}
.tagline{top:543px;font-family:'Raleway',sans-serif;font-weight:300;font-size:31px;line-height:34px;color:var(--white)}

/* value chain */
.chain{top:748px;left:0;width:1200px;height:589px;background:linear-gradient(180deg,#fff 0%,#f6f6f6 60%,#fff 100%)}
.h2{font-family:'Questrial',sans-serif;font-weight:700;color:var(--ink)}
.h2 em{font-style:normal;color:var(--accent)}
.rule{width:52px;height:2px;background:var(--line);left:574px}
.step-title{font-family:'Questrial',sans-serif;font-weight:700;font-size:22px;line-height:25px;color:var(--accent)}
.step-text{font-size:12.5px;line-height:19.5px;color:var(--accent)}
.right{text-align:right}
.icon-ring{width:60px;height:60px;border-radius:50%;background:var(--white);box-shadow:0 3px 10px rgba(0,0,0,.15)}
.icon-ring svg{position:absolute;left:15px;top:15px}

/* team */
.team{top:1357px;left:0;width:1200px;height:667px;background:linear-gradient(180deg,#f3f3f3,#ececec)}
.sub{font-size:14.5px;color:var(--ink)}
.filters{top:1591px;font-size:13px;letter-spacing:1px;color:var(--muted)}
.filters .on{color:var(--accent);font-weight:700}
.filters .sep{margin:0 22px;color:#aaa}
.photo{top:1657px;width:243px;height:247px;background:linear-gradient(180deg,#c8c8c8,#8e8e8e)}
.card-hover{top:1657px;left:844px;width:245px;height:247px;background:linear-gradient(180deg,#444,#2a2a2a);color:var(--white);text-align:center}
.card-name{margin-top:78px;font-family:'Questrial',sans-serif;font-weight:700;font-size:21px}
.card-role{margin-top:6px;font-size:11.5px;letter-spacing:.5px}
.card-plus{width:38px;height:38px;border:1.5px solid var(--white);border-radius:50%;margin:18px auto 0;line-height:34px;font-size:22px}

/* contact */
.contact{top:2024px;left:0;width:1200px;height:412px;background:radial-gradient(ellipse at 50% 60%,#5a5a5a 0%,#333 45%,#1c1c1c 100%)}
.btn{top:2259px;width:158px;height:48px;border-radius:24px;font-size:12px;letter-spacing:1px;line-height:46px;text-align:center}
.btn-solid{left:436px;background:var(--white);color:var(--accent)}
.btn-ghost{left:608px;border:1px solid var(--white);color:var(--white)}

/* find us */
.circle{width:94px;height:94px;border-radius:50%;background:var(--white);box-shadow:0 3px 12px rgba(0,0,0,.15)}
.circle svg{position:absolute;left:27px;top:27px}
.label{font-family:'Tinos',serif;font-size:16px;color:var(--ink);width:360px;text-align:center}
.value{font-size:15.5px;color:var(--ink);width:360px;text-align:center}

/* footer */
.footer{top:2927px;left:0;width:1200px;height:328px;background:radial-gradient(ellipse at 50% 40%,#4a4a4a 0%,#383838 60%,#2a2a2a 100%)}
.foot-dot{top:2970px;left:585px;width:30px;height:30px;border:2px solid var(--white);border-radius:50%}
.foot-name{top:3006px;font-family:'Questrial',sans-serif;font-size:18px;letter-spacing:1px;color:var(--white)}
.foot-links{top:3049px;font-size:12px;color:var(--white)}
.foot-links .sep{margin:0 16px;opacity:.6}
.social{top:3095px;width:42px;height:42px;border:1.5px solid var(--white);border-radius:50%}
.copy{top:3214px;font-size:12.5px;color:var(--white)}
</style>
</head>
<body>

<!-- Hero -->
<section class="hero abs" role="img" aria-label="Dark blurred plant foliage background"></section>
<div class="brand abs"><span class="brand-dot"></span>Verdant Ridge Capital</div>
<div class="lang abs" role="img" aria-label="Language flag"></div>
<div class="lang-caret abs"></div>
<nav>
  <span class="nav abs" style="left:709px">INVESTMENT FOCUS</span>
  <span class="nav abs" style="left:913px">TEAM</span>
  <span class="nav abs" style="left:1011px">CONTACTS</span>
</nav>
<div class="video abs" role="img" aria-label="Video still of a plant close-up"></div>
<div class="play abs"><svg width="80" height="80"><polygon points="33,27 33,53 54,40" fill="#fff"/></svg></div>
<p class="tagline abs center">Or goal is to leverage growth of the global cannabis<br>industry by investing in public and private equity of<br>companies in this sector</p>

<!-- Value chain -->
<section class="chain abs" aria-label="Investment focus"></section>
<h2 class="h2 abs center" style="top:817px;font-size:30px">We invest across all steps of the cannabis-product value chain</h2>
<div class="rule abs" style="top:873px"></div>

<svg class="abs" style="left:471px;top:941px" width="258" height="258">
  <circle cx="129" cy="129" r="109" fill="none" stroke="#2b2b2b" stroke-width="40"/>
</svg>

<h3 class="step-title abs right" style="top:924px;left:96px;width:200px">Cultivation</h3>
<p class="step-text abs right" style="top:956px;left:96px;width:200px">Cultivation facilities – high tech green houses aimed to reduce operational costs and maximize quality of flowers and pre-rolls</p>
<div class="icon-ring abs" style="left:317px;top:929px"><svg width="30" height="30" fill="none" stroke="#2b2b2b" stroke-width="1.5"><path d="M15 28V12M15 14c-6 0-9-4-9-8 5 0 9 3 9 8zM15 12c0-5 4-8 9-8 0 4-3 8-9 8z"/></svg></div>

<h3 class="step-title abs right" style="top:1087px;left:96px;width:200px">Value Added<br>Retail Products</h3>
<p class="step-text abs right" style="top:1143px;left:96px;width:200px">Value added products in several sectors: Health and Beauty, Pharmaceutical products, food and beverages</p>
<div class="icon-ring abs" style="left:317px;top:1092px"><svg width="30" height="30" fill="none" stroke="#2b2b2b" stroke-width="1.5"><rect x="4" y="8" width="22" height="19"/><path d="M4 14h22M10 8V4h10v4"/></svg></div>

<h3 class="step-title abs" style="top:924px;left:890px;width:220px">Processing</h3>
<p class="step-text abs" style="top:956px;left:892px;width:200px">High quality THC and CBD concentrates used for the enrichment of FMCG or medical end products as well as concentrates available for the direct retail consumption (such as oil and powders)</p>
<div class="icon-ring abs" style="left:808px;top:929px"><svg width="30" height="30" fill="none" stroke="#2b2b2b" stroke-width="1.5"><circle cx="12" cy="17" r="6"/><circle cx="12" cy="17" r="2"/><circle cx="23" cy="8" r="4"/><path d="M12 8v3M12 23v3M3 17h3M18 17h3"/></svg></div>

<h3 class="step-title abs" style="top:1112px;left:890px;width:220px">Distribution</h3>
<p class="step-text abs" style="top:1144px;left:892px;width:200px">Promising tools of distribution within the cannabis industry: e-shops, coffee shop branches etc.</p>
<div class="icon-ring abs" style="left:808px;top:1118px"><svg width="30" height="30" fill="none" stroke="#2b2b2b" stroke-width="1.5"><circle cx="15" cy="15" r="3"/><path d="M15 3v9M15 18v9M3 15h9M18 15h9M7 7l6 6M17 17l6 6M23 7l-6 6M7 23l6-6"/></svg></div>

<!-- Team -->
<section class="team abs" aria-label="Our team"></section>
<h2 class="h2 abs center" style="top:1440px;font-size:30px;font-weight:400">Our <em style="font-weight:700">Team</em></h2>
<p class="sub abs center" style="top:1508px">Reiciendis voluptatibus maiores alias consequatur aut perferendis doloribus</p>
<div class="filters abs center"><span class="on">ALL</span><span class="sep">/</span>INVESTMENT TEAM<span class="sep">/</span>ADVISORY BOARD</div>
<div class="photo abs" style="left:112px" role="img" aria-label="Portrait photo of a team member"></div>
<div class="photo abs" style="left:356px" role="img" aria-label="Portrait photo of a team member"></div>
<div class="photo abs" style="left:600px" role="img" aria-label="Portrait photo of a team member"></div>
<div class="card-hover abs" role="img" aria-label="Portrait photo of an advisory board member with dark overlay">
  <div class="card-name">Lucas Marten</div>
  <div class="card-role">ADVISORY BOARD MEMBER</div>
  <div class="card-plus">+</div>
</div>

<!-- Contact -->
<section class="contact abs" role="img" aria-label="Digital globe and network background"></section>
<h2 class="abs center" style="top:2116px;font-family:'Questrial',sans-serif;font-weight:700;font-size:30px;color:#fff">Contact Us</h2>
<div class="abs" style="top:2165px;left:574px;width:52px;height:2px;background:#fff"></div>
<p class="abs center" style="top:2186px;font-size:14.5px;color:#fff">If you are an investor interested in learning more about our fund, please send us a message</p>
<a class="btn btn-solid abs">SEND MESSAGE</a>
<a class="btn btn-ghost abs">LEARN MORE</a>

<!-- Find us -->
<h2 class="h2 abs center" style="top:2510px;font-size:30px;font-weight:400">How to <em style="font-weight:700">Find Us</em></h2>
<div class="rule abs" style="top:2558px"></div>
<p class="sub abs center" style="top:2580px">At vero eos et accusamus et iusto odio dignissimos ducimus qui blanditiis praesentium</p>

<div class="circle abs" style="left:241px;top:2658px"><svg width="40" height="40" fill="none" stroke="#2b2b2b" stroke-width="1.6"><path d="M9 5l6 6-3 4c2 5 6 9 11 11l4-3 6 6-4 5C17 34 6 23 4 9z"/></svg></div>
<div class="circle abs" style="left:553px;top:2658px"><svg width="40" height="40" fill="none" stroke="#2b2b2b" stroke-width="1.6"><path d="M20 30C13 21 11 17 11 13a9 9 0 0118 0c0 4-2 8-9 17z"/><circle cx="20" cy="13" r="3"/><path d="M12 26l-8 9h32l-8-9"/></svg></div>
<div class="circle abs" style="left:868px;top:2658px"><svg width="40" height="40" fill="none" stroke="#2b2b2b" stroke-width="1.6"><rect x="4" y="12" width="32" height="22"/><path d="M4 12l16 12 16-12M4 34l12-10M36 34L24 24M10 12V5h20v7"/></svg></div>

<div class="label abs" style="left:108px;top:2776px">PHONE</div>
<div class="value abs" style="left:108px;top:2806px">+01 2345 67890</div>
<div class="label abs" style="left:420px;top:2776px">ADDRESS</div>
<div class="value abs" style="left:420px;top:2806px">Street Name, City Name, Country Code</div>
<div class="label abs" style="left:735px;top:2776px">EMAIL</div>
<div class="value abs" style="left:735px;top:2806px">info@domainname.com</div>

<!-- Footer -->
<footer class="footer abs" role="img" aria-label="Leaf-textured background"></footer>
<div class="foot-dot abs"></div>
<div class="foot-name abs center">Verdant Ridge Capital</div>
<div class="foot-links abs center">Investment Focus<span class="sep">|</span>Team<span class="sep">|</span>Contacts</div>
<div class="social abs" style="left:554px" aria-label="Social link"></div>
<div class="social abs" style="left:604px" aria-label="Social link"></div>
<div class="copy abs center">Copyrights © 2019, Verdant Ridge Capital. All rights reserved.</div>

</body>
</html>
```